Business card design needed

I would like a one sided black business card with the information provided above. Refer to my website www.lobcrafttennis.com.au for an example of colors I have used for my site, would like to keep this consistent for my business cards also, I will upload my logo below.

I am a new small business that provides tennis customers with racquet re stringing, tennis strings and accessories.

Industry/Entity Type

Small Business

Contact Information for Business Card

Lob Craft Tennis

Dennis Morrow
Managing Director

lobcrafttennis@mailbay.com
www.lobcrafttennis.com.au
0412 695 203

Racquet Restringing/Tennis Strings/Accessories

Requirements
Must have
• Must have my logo and card must be black

```html
<!DOCTYPE html>
<html lang="en">
<head>
<meta charset="utf-8">
<title>Lob Craft Tennis – Business Card</title>
<link rel="stylesheet" href="https://fonts.googleapis.com/css2?family=Arimo:ital,wght@0,400;0,700;1,400&display=swap">
<style>
  :root {
    --card-black: #000000;
    --lime: #b5e61d;
    --paper: #ffffff;
    --ink: #111111;
    --stage: #ece7df;
    --ball-blue: #2f6fb5;
  }
  * { box-sizing: border-box; margin: 0; padding: 0; }
  html, body {
    width: 1200px; height: 890px; overflow: hidden;
    background: var(--stage);
    font-family: "Arimo", Arial, sans-serif;
  }
  .stage { position: relative; width: 1200px; height: 890px; }

  .card {
    position: absolute;
    width: 608px; height: 357px;
    background: var(--card-black);
    overflow: hidden;
  }
  .card--logo { left: 64px; top: 133px; border: 1px solid #cfcfcf; }
  .card--details { left: 385px; top: 501px; background: var(--paper); border: 2px solid var(--card-black); }

  .brand {
    position: absolute;
    display: flex; align-items: center; gap: 14px;
    transform: translateX(-50%);
    white-space: nowrap;
  }
  .brand__dot {
    width: 34px; height: 34px; border-radius: 50%;
    background: var(--lime);
  }
  .brand__name {
    font-weight: 700; font-size: 40px; letter-spacing: 1px;
    color: var(--lime); text-transform: uppercase;
  }
  .card--logo .brand { left: 50%; top: 150px; }

  .details__head {
    position: absolute; left: 0; top: 0; width: 100%; height: 164px;
    background: var(--card-black);
  }
  .card--details .brand { left: 50%; top: 50px; }
  .brand--small .brand__name { font-size: 34px; }
  .brand--small .brand__dot { width: 28px; height: 28px; }

  .details__rule {
    position: absolute; left: 72px; top: 155px;
    width: 457px; height: 6px; border-radius: 3px;
    background: var(--lime);
  }

  .person { position: absolute; left: 385px; top: 168px; color: var(--ink); }
  .person__name { font-size: 31px; line-height: 1.1; }
  .person__role { font-size: 24px; font-style: italic; margin-top: 4px; }

  .contact {
    position: absolute; left: 4px; top: 232px;
    list-style: none; font-style: italic; font-size: 19px; color: var(--ink);
  }
  .contact li { display: flex; align-items: center; gap: 4px; height: 25.5px; }
  .contact svg { width: 22px; height: 22px; flex: none; }

  .services {
    position: absolute; left: 0; bottom: 0; width: 100%; height: 38px;
    background: var(--lime); border-top: 2px solid var(--card-black);
    display: flex; align-items: center; justify-content: center;
    font-style: italic; font-size: 22px; color: var(--ink);
  }
</style>
</head>
<body>
<main class="stage">

  <section class="card card--logo" aria-label="Card front">
    <div class="brand">
      <span class="brand__dot"></span>
      <span class="brand__name">Lob Craft Tennis</span>
    </div>
  </section>

  <section class="card card--details" aria-label="Card back">
    <div class="details__head">
      <div class="brand brand--small">
        <span class="brand__dot"></span>
        <span class="brand__name">Lob Craft Tennis</span>
      </div>
      <div class="details__rule"></div>
    </div>

    <div class="person">
      <p class="person__name">Dennis Morrow</p>
      <p class="person__role">Managing Director</p>
    </div>

    <ul class="contact">
      <li>
        <svg viewBox="0 0 24 24" aria-hidden="true"><circle cx="12" cy="12" r="10.5" fill="none" stroke="#111" stroke-width="1.6"/><path d="M8 6.5l2 2.5-1.2 1.5c.8 1.8 2.1 3.1 3.9 3.9l1.5-1.2 2.5 2-1.3 2c-4.5-.4-8.3-4.2-8.7-8.7z" fill="#111"/></svg>
        <span>0412 695 203</span>
      </li>
      <li>
        <svg viewBox="0 0 24 24" aria-hidden="true"><rect x="3" y="6" width="18" height="12" fill="none" stroke="#111" stroke-width="1.6"/><path d="M3 6l9 7 9-7M3 18l7-6M21 18l-7-6" fill="none" stroke="#111" stroke-width="1.4"/></svg>
        <span>lobcrafttennis@mailbay.com</span>
      </li>
      <li>
        <svg viewBox="0 0 24 24" aria-hidden="true"><circle cx="12" cy="12" r="10.5" fill="none" stroke="#111" stroke-width="1.6"/><circle cx="12" cy="12" r="4" fill="none" stroke="#111" stroke-width="1.8"/></svg>
        <span>www.lobcrafttennis.com.au</span>
      </li>
    </ul>

    <p class="services">Racquet Restringing/Tennis Strings/Accessories</p>
  </section>

</main>
</body>
</html>
```